Poster design for the WILLOW WISP magic show.

We need a poster design for our magic show. This isn't your typical 'small town' magic show. Our show features world class magicians from the Velvet Lantern, in Hollywood California. The show is geared toward everyone, it is family friendly - with a little bit of an edge. We want people to see the poster and feel like they are going to have a unique and sophisticated magical experience. We also want individuals and couples to see the poster and feel like it is a show for them and not only for children.
Updates

Target Market(s)

BRT audience, family audience, the age range is anywhere from 5 - 105. Cool people.

Industry/Entity Type

Town

Requirements
Must have
• Our attached .jpg of the magician floating in the air. Poster size 24x36"
Must have text:
The 3rd Annual Albuquerque Conjuring Gala Presents (small type)
Willow Wisp (should be larger type)
November 24th - 25th
Showtimes 3:00PM & 7:30PM Saturday, 2:00PM Sunday
Tickets available at www.DorvaSeats.example For more information contact Dorva Theatre @ 505.555.0147
Nice to have
• A sort of old school/antique feeling to the poster.
Perhaps a theater marquee
Check out www.grovelumen.example - we love the feeling of this site for our poster...
Feel free to adjust the provided .jpg accordingly in regards to color/size/interaction with the rest of the poster
Should not have
• Should not have clowns, bunnies, anything that would make it feel like a 3 year old's magic themed birthday party.

```html
<!DOCTYPE html>
<html lang="en">
<head>
<meta charset="utf-8">
<title>Willow Wisp – Poster</title>
<link rel="stylesheet" href="https://fonts.googleapis.com/css2?family=Bebas+Neue&family=Jost:wght@400;500&display=swap">
<style>
  :root {
    --backdrop-dark: #4a1f0c;
    --backdrop-mid: #6e3a17;
    --backdrop-light: #8a5a2c;
    --poster-black: #0f0a06;
    --poster-brown: #2a1a0c;
    --gold: #e5b021;
    --gold-deep: #c98a14;
    --title-shadow: #7a1410;
    --url-red: #c8301e;
    --stage-floor: #6a3a1c;
  }
  * { margin: 0; padding: 0; box-sizing: border-box; }
  html, body { width: 1200px; height: 900px; overflow: hidden; }
  body {
    position: relative;
    background: linear-gradient(100deg, var(--backdrop-dark) 0%, var(--backdrop-mid) 45%, var(--backdrop-light) 100%);
    font-family: "Jost", "Century Gothic", sans-serif;
  }
  .poster {
    position: absolute; left: 300px; top: 0; width: 600px; height: 900px;
    background: radial-gradient(ellipse at 50% 45%, var(--poster-brown) 0%, var(--poster-black) 75%);
    overflow: hidden;
  }
  .presenter {
    position: absolute; top: 22px; width: 100%; text-align: center;
    color: var(--gold); font-size: 17px; font-weight: 500; letter-spacing: 0.2px;
  }
  .title { position: absolute; left: 60px; top: 42px; width: 480px; height: 180px; }
  .title text { font-family: "Bebas Neue", Impact, sans-serif; }
  .stage-photo {
    position: absolute; left: 0; top: 240px; width: 600px; height: 395px;
    background:
      radial-gradient(ellipse at 32% 55%, rgba(214,150,70,0.55) 0%, rgba(120,70,30,0.2) 35%, transparent 60%),
      radial-gradient(ellipse at 65% 20%, rgba(190,80,60,0.35) 0%, transparent 45%),
      linear-gradient(180deg, #20140b 0%, #4a3018 70%, #5a3a1e 100%);
  }
  .stage-floor {
    position: absolute; left: 0; top: 633px; width: 600px; height: 3px;
    background: var(--stage-floor);
  }
  .dates {
    position: absolute; top: 679px; left: 62px; width: 476px;
    display: flex; align-items: center; justify-content: space-between;
  }
  .dates-text { color: var(--gold); font-size: 20px; font-weight: 500; white-space: nowrap; padding: 0 8px; }
  .dates-text sup { font-size: 12px; vertical-align: 1px; }
  .rule-stack { display: flex; flex-direction: column; gap: 3px; }
  .rule-stack span { display: block; height: 1px; background: var(--gold-deep); }
  .rule-stack.left { align-items: flex-end; }
  .rule-stack.right { align-items: flex-start; }
  .showtimes {
    position: absolute; left: 62px; top: 755px; width: 480px;
    transform: rotate(-5.5deg); transform-origin: center;
    color: var(--gold); font-size: 17px; font-weight: 500; font-style: italic;
    text-align: center; padding: 3px 0;
    border-top: 1px solid var(--gold-deep); border-bottom: 1px solid var(--gold-deep);
    white-space: nowrap;
  }
  .showtimes sup { font-size: 11px; }
  .tickets {
    position: absolute; top: 838px; width: 100%; text-align: center;
    color: var(--gold-deep); font-size: 14px; line-height: 21px;
  }
  .tickets .url { color: var(--url-red); letter-spacing: 5px; }
</style>
</head>
<body>
  <main class="poster">
    <p class="presenter">THE 3RD ANNUAL ALBUQUERQUE CONJURING GALA PRESENTS</p>

    <svg class="title" viewBox="0 0 480 180" aria-label="Willow Wisp">
      <defs>
        <linearGradient id="titleGold" x1="0" y1="0" x2="0" y2="1">
          <stop offset="0" stop-color="#f2c63a"/>
          <stop offset="1" stop-color="#c98a14"/>
        </linearGradient>
      </defs>
      <text x="3" y="161" font-size="170" textLength="474" lengthAdjust="spacingAndGlyphs" fill="var(--title-shadow)">WILLOW WISP</text>
      <text x="0" y="155" font-size="170" textLength="474" lengthAdjust="spacingAndGlyphs" fill="url(#titleGold)">WILLOW WISP</text>
    </svg>

    <div class="stage-photo" role="img" aria-label="Photograph: magician levitating beside a floating chair on a spotlit stage"></div>
    <div class="stage-floor"></div>

    <div class="dates">
      <div class="rule-stack left"><span style="width:60px"></span><span style="width:90px"></span><span style="width:120px"></span></div>
      <p class="dates-text">NOVEMBER 24<sup>TH</sup> - 25<sup>TH</sup></p>
      <div class="rule-stack right"><span style="width:60px"></span><span style="width:90px"></span><span style="width:120px"></span></div>
    </div>

    <p class="showtimes">SHOWTIMES 3:00<sup>PM</sup> &amp; 7:30<sup>PM</sup> SATURDAY, 2:00<sup>PM</sup> SUNDAY</p>

    <div class="tickets">
      <p>TICKETS AVAILABLE AT <span class="url">WWW.DORVASEATS.EXAMPLE</span></p>
      <p>FOR MORE INFORMATION CONTACT DORVA THEATRE @ 505.555.0147</p>
    </div>
  </main>
</body>
</html>
```